Casino Rental Business Trade Show Banner

I am looking for a trade show banner to set up on a floor display 27inch x 81inc. I would like it to advertise that we are a casino rental business based in the Chicagoland area. We have all the Casino gaming tables with dealers and we can do events as small as 1 table and enough to accommodate 1000's of people. This banner will be going into a trade show environment. We want to get people attention and let them know we can do this for there charity or corporate event.

Target Market(s)

Corporate and Charity casino nights... Holiday parties or employee apperication party

Industry/Entity Type

Casino

Font styles to use
Serif

Requirements
Must have
• my company info.
• pictures of equipment
• general casino theme
Nice to have
• website company theme
• call to action
Should not have
• anything about winning real money.
• no women on sexy images.... This for corporate enviroment

```html
<!DOCTYPE html>
<html lang="en">
<head>
<meta charset="utf-8">
<title>Lakefront Casino Events – Trade Show Banner</title>
<link rel="stylesheet" href="https://fonts.googleapis.com/css2?family=Cinzel:wght@400&family=Crimson+Pro:wght@400&family=Crimson+Text:wght@400&family=Open+Sans:wght@400;700&display=swap">
<style>
  :root {
    --stage: #2b2b2b;
    --ink-black: #1f1f1f;
    --gold: #d4a43a;
    --gold-light: #f0c75e;
    --gold-dark: #8a6418;
    --casino-red: #9e1b1c;
    --casino-red-dark: #6e0f10;
    --text-light: #f4efe6;
    --felt-green: #1f5a3a;
  }
  html, body {
    margin: 0;
    padding: 0;
    width: 1200px;
    height: 900px;
    overflow: hidden;
    background: var(--stage);
  }
  .canvas {
    position: relative;
    width: 1200px;
    height: 900px;
  }
  .banner {
    position: absolute;
    left: 415px;
    top: 15px;
    width: 370px;
    height: 870px;
    overflow: hidden;
    background: var(--ink-black);
  }
  .banner-art {
    position: absolute;
    inset: 0;
    width: 370px;
    height: 870px;
  }
  .brand-mark {
    position: absolute;
    left: 165px;
    top: 18px;
    width: 38px;
    height: 38px;
    border: 3px solid var(--gold);
    box-sizing: border-box;
    border-radius: 4px;
  }
  .brand-name {
    position: absolute;
    left: 0;
    right: 0;
    top: 62px;
    margin: 0;
    text-align: center;
    font-family: "Crimson Text", serif;
    font-weight: 400;
    font-size: 31px;
    line-height: 1;
    color: var(--text-light);
  }
  .headline {
    position: absolute;
    left: 32px;
    top: 540px;
    margin: 0;
    font-family: "Cinzel", serif;
    font-weight: 400;
    color: var(--text-light);
    line-height: 1;
  }
  .headline .small { font-size: 22px; }
  .headline .large { font-size: 44px; }
  .headline .line-one { display: block; }
  .headline .line-two { display: block; padding-left: 64px; margin-top: -6px; }
  .pitch {
    position: absolute;
    left: 16px;
    right: 16px;
    top: 637px;
    margin: 0;
    text-align: center;
    font-family: "Crimson Pro", serif;
    font-size: 14px;
    line-height: 23.5px;
    text-transform: uppercase;
    color: var(--gold);
  }
  .event-types {
    position: absolute;
    left: 0;
    right: 0;
    top: 719px;
    margin: 0;
    padding: 0;
    list-style: none;
    display: flex;
    justify-content: center;
    gap: 7px;
    font-family: "Crimson Text", serif;
    font-size: 13px;
    color: var(--text-light);
  }
  .event-types li + li::before {
    content: "•";
    margin-right: 7px;
  }
  .social-links {
    position: absolute;
    left: 0;
    right: 0;
    top: 752px;
    display: flex;
    justify-content: center;
    gap: 4px;
  }
  .social-links span {
    width: 16px;
    height: 16px;
    border-radius: 2px;
    background: var(--gold);
  }
  .contact {
    position: absolute;
    left: 0;
    right: 0;
    top: 810px;
    text-align: center;
    font-family: "Open Sans", sans-serif;
    color: var(--text-light);
  }
  .contact .call {
    display: flex;
    justify-content: center;
    align-items: center;
    gap: 4px;
    font-size: 15px;
    line-height: 20px;
    color: var(--gold);
  }
  .contact .call strong { font-weight: 700; }
  .contact .call svg { width: 11px; height: 11px; }
  .contact .web {
    font-size: 17px;
    line-height: 24px;
    margin-top: 2px;
  }
</style>
</head>
<body>
<main class="canvas">
  <section class="banner" aria-label="Lakefront Casino Events trade show banner">
    <svg class="banner-art" viewBox="0 0 455 1070" preserveAspectRatio="none">
      <defs>
        <linearGradient id="photoTones" x1="0" y1="0" x2="0" y2="1">
          <stop offset="0" stop-color="#c8551c"/>
          <stop offset="0.35" stop-color="#8a4a2e"/>
          <stop offset="0.58" stop-color="#3d2a26"/>
          <stop offset="0.7" stop-color="#1f5a3a"/>
          <stop offset="1" stop-color="#173f2b"/>
        </linearGradient>
        <linearGradient id="insetTones" x1="0" y1="0" x2="1" y2="1">
          <stop offset="0" stop-color="#3a3025"/>
          <stop offset="0.5" stop-color="#7a2a22"/>
          <stop offset="1" stop-color="#b0262a"/>
        </linearGradient>
        <linearGradient id="goldSheen" x1="0" y1="0" x2="1" y2="0">
          <stop offset="0" stop-color="#8a6418"/>
          <stop offset="0.5" stop-color="#f0c75e"/>
          <stop offset="1" stop-color="#b78a2c"/>
        </linearGradient>
        <radialGradient id="redGlow" cx="0.5" cy="0.4" r="0.7">
          <stop offset="0" stop-color="#a81f20"/>
          <stop offset="1" stop-color="#6e0f10"/>
        </radialGradient>
      </defs>

      <!-- red lower panel -->
      <rect x="0" y="480" width="455" height="560" fill="url(#redGlow)"/>

      <!-- event photo area -->
      <path d="M0,300 Q170,175 455,168 L455,505 Q330,640 0,650 Z" fill="url(#photoTones)" role="img" aria-label="Photo of smiling guests gathered around a craps table, dice in the air"/>

      <!-- gold sweep above photo -->
      <path d="M0,300 Q170,175 455,168 L455,148 Q170,150 0,290 Z" fill="url(#goldSheen)"/>

      <!-- gold sweep below photo -->
      <path d="M0,650 Q330,640 455,505 L455,520 Q340,660 0,665 Z" fill="url(#goldSheen)"/>

      <!-- round equipment inset -->
      <circle cx="354" cy="580" r="88" fill="url(#goldSheen)"/>
      <circle cx="354" cy="580" r="80" fill="url(#insetTones)" role="img" aria-label="Photo of a roulette wheel and table overlooking a city skyline"/>

      <!-- footer -->
      <path d="M0,990 Q228,930 455,990 L455,1070 L0,1070 Z" fill="url(#goldSheen)"/>
      <path d="M0,1002 Q228,944 455,1002 L455,1070 L0,1070 Z" fill="#222222"/>
    </svg>

    <span class="brand-mark" aria-hidden="true"></span>
    <h1 class="brand-name">Lakefront Casino Events</h1>

    <h2 class="headline">
      <span class="line-one"><span class="small">BRINGING </span><span class="large">VEGAS</span></span>
      <span class="line-two"><span class="small">TO </span><span class="large">CHICAGO</span></span>
    </h2>

    <p class="pitch">For over 30 years, we've been bringing<br>the party to Chicago. Let us bring Vegas<br>to your next event!</p>

    <ul class="event-types">
      <li>Charity Events</li>
      <li>Corporate Events</li>
      <li>Private Events</li>
    </ul>

    <div class="social-links" aria-label="Social media links">
      <span></span><span></span><span></span><span></span>
    </div>

    <div class="contact">
      <div class="call">
        <svg viewBox="0 0 24 24" aria-hidden="true"><path fill="currentColor" d="M6.6 10.8a15.1 15.1 0 0 0 6.6 6.6l2.2-2.2a1 1 0 0 1 1-.25 11.4 11.4 0 0 0 3.6.57 1 1 0 0 1 1 1V20a1 1 0 0 1-1 1A17 17 0 0 1 3 4a1 1 0 0 1 1-1h3.5a1 1 0 0 1 1 1c0 1.25.2 2.450.57 3.57a1 1 0 0 1-.25 1z"/></svg>
        <span>CALL TODAY: <strong>1-888-555-0142</strong></span>
      </div>
      <div class="web">www.lakefrontcasinoevents.com</div>
    </div>
  </section>
</main>
</body>
</html>
```